Beachfront Resort Landing Page

I need a design for a landing page related to a Beachfront Costa Rican Resort. This will be used as a Social Media landing page, so conversion is a must. Prefer someone with experience designing single-landing pages for conversions.

Can use this site as a reference for content / info - ramasolvento.com

The landing page needs to contain these items

"Book a 4 night Stay During the Costa Rican Green-Season, and get your 5th night Free at this All Inclusive Luxury Beachfront Resort!"

"As a Bonus, we'll throw in any of these Activities or Tours for Free! Don't wait! These will fill up fast."
"Free Massage"
"Night Hike"
"Birdwatching Tour"
"Max 2 per booking, can mix-match. While supplies last. Must redeemed during this stay" (in small print under text / images)

Also highlight these items too please

"Accessible only via boat, this Costa Rican Luxury Paradise is perfect for those wanting to escape the crowds, enjoy amazing cuisine, while swimming in our beachfront pool, and more"

"Green Season is known for whale migrations, enjoy watching the marine life from our beachfront location, or up close and personal via kayak or paddleboard"

"Paddleboards, kayaks, snorkeling gear, and more are free during your stay."

"Enjoy fresh cuisine and unique beverages daily"

"Nubeway Internet Access Included with all Bookings"

The landing page must have
- A contact form close to above the fold area
- Booking dates function around the same area
- CTA's related to most of whats mentioned above
- Can use images from the real site - ramasolvento.com
- Areas for videos on the landing page
- Must resemble a good landing page design for conversion, not a standard web-page. Those who know, will know.

Please let me know if you have any questions.

```html
<!DOCTYPE html>
<html lang="en">
<head>
<meta charset="utf-8">
<title>Rama Sol Vento – Green Season Offer</title>
<link href="https://fonts.googleapis.com/css2?family=Inter:wght@300;400;500;600;700&display=swap" rel="stylesheet">
<style>
:root{
  --green:#0f7a3a;
  --green-dark:#0b5e2c;
  --forest:#2f6b4d;
  --forest-deep:#245a3f;
  --paper:#efefef;
  --white:#ffffff;
  --ink:#2b2b2b;
  --muted:#6a6a6a;
  --line:#d9d9d9;
  --feature-green:#1e6b3c;
}
*{box-sizing:border-box;margin:0;padding:0}
html,body{width:1200px;height:4115px;overflow:hidden;background:var(--white)}
body{font-family:"Inter",sans-serif;color:var(--ink)}
.page{position:relative;width:1200px;height:4115px;overflow:hidden}

/* hero */
.hero{position:absolute;left:0;top:0;width:1200px;height:507px;
  background:linear-gradient(180deg,#1f3a2c 0%,#2d5248 40%,#3f7a82 65%,#2e4a3e 100%)}
.hero-photo{position:absolute;inset:0}
.hero-bar{position:absolute;top:36px;left:200px;right:200px;display:flex;justify-content:space-between;align-items:center;color:var(--white)}
.hero-phone{font-size:13px;display:flex;align-items:center;gap:6px;width:170px}
.brand{display:flex;flex-direction:column;align-items:center;gap:6px;color:var(--white)}
.brand-dot{width:34px;height:34px;border-radius:50%;background:var(--white)}
.brand-name{font-size:14px;font-weight:400;letter-spacing:.5px}
.btn-ghost{border:1px solid var(--white);color:var(--white);font-size:11px;font-weight:600;padding:9px 20px;border-radius:2px;width:108px;text-align:center}
.hero-title{position:absolute;top:200px;left:180px;right:180px;text-align:center;color:var(--white);font-size:25px;font-weight:300;line-height:1.38}
.hero-title b{font-weight:700}
.btn{display:inline-block;background:var(--green);color:var(--white);font-size:11px;font-weight:600;padding:9px 20px;border-radius:2px}
.hero-cta{position:absolute;top:315px;left:0;right:0;text-align:center}

/* booking */
.booking{position:absolute;top:447px;left:162px;width:874px;height:104px;background:var(--white);border-radius:6px;box-shadow:0 6px 18px rgba(0,0,0,.15);display:flex;align-items:center;padding:0 36px;gap:14px;z-index:2}
.field{display:flex;flex-direction:column;gap:8px}
.field label{font-size:10px;font-weight:600}
.field .input{border:1px solid var(--line);height:34px;border-radius:3px;font-size:11px;display:flex;align-items:center;justify-content:space-between;padding:0 10px;color:var(--ink)}
.f-date .input{width:160px}
.f-num .input{width:86px}
.booking .btn{margin-top:20px;padding:11px 0;width:150px;text-align:center;background:var(--green-dark)}

/* bonus */
.bonus{position:absolute;top:507px;left:0;width:1200px;height:585px;background:var(--green);color:var(--white);text-align:center}
.bonus h2{margin-top:125px;font-size:27px;font-weight:400;line-height:1.35}
.activities{display:flex;gap:25px;justify-content:center;margin-top:30px}
.activity{width:249px;height:191px;background:var(--white);border-radius:3px;overflow:hidden;color:var(--ink)}
.activity .pic{height:152px}
.activity p{font-size:15px;line-height:39px}
.fine{font-size:9px;margin-top:37px}
.btn-outline{display:inline-block;margin-top:28px;border:1px solid var(--white);font-size:10px;font-weight:600;padding:10px 0;width:115px;border-radius:2px}

/* features */
.features{position:absolute;top:1092px;left:0;width:1200px;height:1439px;background:linear-gradient(180deg,#f1f1f1,#e9e9e9)}
.feature{position:absolute;left:200px;width:797px;height:235px}
.feature .pic{position:absolute;top:0;width:387px;height:235px;border-radius:3px}
.feature .txt{position:absolute;top:0;height:235px;width:345px;display:flex;align-items:center;font-size:15px;line-height:1.95;color:var(--feature-green)}
.feature .txt b{font-weight:600}
.feature .link{position:absolute;top:117px;width:32px;height:2px;background:var(--feature-green)}
.feature.left .pic{left:0}.feature.left .txt{left:452px}.feature.left .link{left:387px}
.feature.right .pic{left:410px}.feature.right .txt{left:0}.feature.right .link{left:378px}

/* videos */
.videos{position:absolute;top:2531px;left:0;width:1200px;height:326px;display:flex;gap:6px}
.video{flex:1;position:relative}
.play{position:absolute;left:50%;top:50%;width:56px;height:56px;margin:-28px 0 0 -28px}

/* facilities */
.facilities{position:absolute;top:2857px;left:0;width:1200px;height:610px;background:var(--paper);text-align:center}
.facilities h3{margin-top:55px;font-size:26px;font-weight:600;color:var(--feature-green)}
.facilities h4{font-size:26px;font-weight:400;color:var(--feature-green);margin-top:4px}
.tiles{display:flex;gap:12px;justify-content:center;margin-top:30px}
.tile{width:138px;height:128px;background:var(--white);border-radius:3px;display:flex;flex-direction:column;align-items:center;padding-top:26px;gap:14px;color:var(--feature-green);font-size:10px;line-height:1.3}
.tile svg{width:36px;height:36px;stroke:var(--feature-green);fill:none;stroke-width:1.8}
.call{margin-top:40px;font-size:14px;color:var(--feature-green)}
.facilities .btn{margin-top:22px;width:86px;padding:10px 0}
.partners{display:flex;justify-content:center;align-items:center;gap:66px;margin-top:52px}
.badge{background:#c9c9c9}
.badge.sq{width:48px;height:64px;border-radius:4px}
.badge.wide{width:120px;height:30px;border-radius:4px}

/* contact */
.map{position:absolute;top:3467px;left:0;width:1200px;height:205px;background:linear-gradient(90deg,#55d3e6 0%,#5fd0e0 40%,#e4ecd9 52%,#d7e6c9 100%)}
.contact-band{position:absolute;top:3672px;left:0;width:1200px;height:443px;background:var(--forest)}
.contact{position:absolute;top:3590px;left:200px;width:800px;height:386px;display:flex;z-index:2}
.contact-info{width:399px;background:var(--forest-deep);color:var(--white);padding:52px 0 0 66px}
.contact-info h5{font-size:16px;font-weight:400;margin-bottom:26px}
.row{display:flex;gap:12px;font-size:12px;line-height:1.9;align-items:flex-start}
.row svg{width:12px;height:12px;margin-top:5px;stroke:var(--white);fill:none;stroke-width:2;flex:none}
.row small{font-size:9px;display:block;line-height:1.4}
.btn-dir{display:inline-block;margin-top:22px;border:1px solid var(--white);font-size:10px;font-weight:600;padding:9px 0;width:126px;text-align:center;border-radius:3px}
.socials{display:flex;gap:8px;margin-top:30px}
.socials span{width:24px;height:24px;border-radius:50%;background:var(--white)}
.contact-form{flex:1;background:var(--white);padding:40px 54px 0 50px}
.contact-form h5{font-size:15px;font-weight:400;color:var(--ink);margin-bottom:24px}
.in{border:1px solid var(--line);height:26px;font-size:8px;color:#555;padding:8px 10px;margin-bottom:16px}
.in.msg{height:58px}
.contact-form .btn{font-size:10px;padding:8px 0;width:88px;text-align:center;margin-top:4px}
.footer{position:absolute;top:4010px;left:0;width:1200px;text-align:center;color:var(--white)}
.footer .brand-dot{width:28px;height:28px}
.footer .brand-name{font-size:11px}
.footer p{font-size:8px;margin-top:12px}
.to-top{position:absolute;top:4052px;left:968px;width:16px;height:16px;stroke:var(--white);fill:none;stroke-width:1.6}
</style>
</head>
<body>
<div class="page">

  <header class="hero">
    <div class="hero-photo" role="img" aria-label="Resort pool surrounded by loungers and tropical palms"></div>
    <div class="hero-bar">
      <div class="hero-phone">
        <svg width="12" height="12" viewBox="0 0 24 24" fill="none" stroke="#fff" stroke-width="2"><path d="M5 3h4l2 5-2.5 1.5a11 11 0 0 0 6 6L16 13l5 2v4a2 2 0 0 1-2 2A16 16 0 0 1 3 5a2 2 0 0 1 2-2z"/></svg>
        (555) 013-4270
      </div>
      <div class="brand"><span class="brand-dot"></span><span class="brand-name">RAMA SOL VENTO</span></div>
      <div style="width:170px;display:flex;justify-content:flex-end"><span class="btn-ghost">Book Now!</span></div>
    </div>
    <h1 class="hero-title"><b>Book a 4 Night Stay</b> During the Costa Rican Green-Season, and <b>Get Your 5th Night Free</b> at this all Inclusive Luxury Beachfront Resort!</h1>
    <div class="hero-cta"><span class="btn">Contact Us</span></div>
  </header>

  <form class="booking">
    <div class="field f-date"><label>Check-in</label><div class="input">1-11-2024<span>▦</span></div></div>
    <div class="field f-date"><label>Check-out</label><div class="input">1-14-2024<span>▦</span></div></div>
    <div class="field f-num"><label>Rooms</label><div class="input">1<span>⌄</span></div></div>
    <div class="field f-num"><label>Adults</label><div class="input">2<span>⌄</span></div></div>
    <div class="field f-num"><label>Children</label><div class="input">1<span>⌄</span></div></div>
    <span class="btn">Book Now!</span>
  </form>

  <section class="bonus">
    <h2>As a bonus, we'll throw in any of these activities or tours<br>for free! Don't wait! These will fill up fast.</h2>
    <div class="activities">
      <div class="activity"><div class="pic" role="img" aria-label="Massage on a beach table by the sea" style="background:linear-gradient(180deg,#c9d6dc,#8c8a7a)"></div><p>Free Massage</p></div>
      <div class="activity"><div class="pic" role="img" aria-label="Night hike in the dark rainforest" style="background:radial-gradient(circle at 45% 45%,#3c4a1a,#0a0d06 70%)"></div><p>Night Hike</p></div>
      <div class="activity"><div class="pic" role="img" aria-label="Bird perched among berries" style="background:linear-gradient(160deg,#6f8a78,#2f4a3a)"></div><p>Birdwatching Tour</p></div>
    </div>
    <p class="fine">*Max 2 per booking, can mix-match. While supplies last. Must redeemed during this stay.</p>
    <span class="btn-outline">Book Now!</span>
  </section>

  <section class="features">
    <div class="feature left" style="top:65px">
      <div class="pic" role="img" aria-label="Boat arriving at the jungle coast" style="background:linear-gradient(180deg,#c8d4dc 0%,#4d7a4a 35%,#3f6b80 60%,#6d8fa0 100%)"></div>
      <span class="link"></span>
      <p class="txt"><span><b>Accessible only via boat,</b><br>this Costa Rican Luxury Paradise is perfect for those wanting to escape the crowds, <b>enjoy amazing cuisine, while swimming in our beachfront pool,</b> and more</span></p>
    </div>
    <div class="feature right" style="top:330px">
      <p class="txt"><span>Green Season is known for whale migrations, <b>enjoy watching the marine life from our beachfront location,</b> or up close and personal via kayak or paddleboard</span></p>
      <span class="link"></span>
      <div class="pic" role="img" aria-label="Snorkeler among coral and tropical fish" style="background:linear-gradient(180deg,#1a6fd0,#0b3f9a)"></div>
    </div>
    <div class="feature left" style="top:596px">
      <div class="pic" role="img" aria-label="Kayakers paddling near a green shoreline" style="background:linear-gradient(180deg,#2f5a2a 0%,#4d7a3a 45%,#7fc0d0 60%,#b5dde2 100%)"></div>
      <span class="link"></span>
      <p class="txt"><span><b>Paddleboards, kayaks, snorkeling gear,</b> and more are free during your stay.</span></p>
    </div>
    <div class="feature right" style="top:861px">
      <p class="txt"><span>Enjoy fresh cuisine and <b>unique beverages daily</b></span></p>
      <span class="link"></span>
      <div class="pic" role="img" aria-label="Plated dishes and cocktails on a wooden table" style="background:linear-gradient(180deg,#8aa03a,#c06a2a 55%,#7a3a1a)"></div>
    </div>
    <div class="feature left" style="top:1127px">
      <div class="pic" role="img" aria-label="Guest relaxing on a lounger by the pool" style="background:linear-gradient(180deg,#3f6a3a 0%,#4fa5b5 50%,#c8a070 100%)"></div>
      <span class="link"></span>
      <p class="txt"><span><b>Nubeway Internet Access Included</b><br>with all Bookings</span></p>
    </div>
  </section>

  <section class="videos">
    <div class="video" role="img" aria-label="Video: aerial view of the jungle beach" style="background:linear-gradient(180deg,#2f5a2a 0%,#4a7a3a 45%,#c7a070 62%,#3aa0b5 80%,#2a8aa5 100%)">
      <svg class="play" viewBox="0 0 56 56"><circle cx="28" cy="28" r="26" fill="none" stroke="#fff" stroke-width="2"/><path d="M23 19l14 9-14 9z" fill="#fff"/></svg>
    </div>
    <div class="video" role="img" aria-label="Video: aerial view of the resort pool" style="background:linear-gradient(180deg,#2f5a2a 0%,#3f7a4a 35%,#3ac0d0 60%,#2a7a6a 100%)">
      <svg class="play" viewBox="0 0 56 56"><circle cx="28" cy="28" r="26" fill="none" stroke="#fff" stroke-width="2"/><path d="M23 19l14 9-14 9z" fill="#fff"/></svg>
    </div>
  </section>

  <section class="facilities">
    <h3>Facilities</h3>
    <h4>Book your stay with us today</h4>
    <div class="tiles">
      <div class="tile"><svg viewBox="0 0 36 36"><path d="M6 14a17 17 0 0 1 24 0M10 19a11 11 0 0 1 16 0M14 24a5 5 0 0 1 8 0"/><circle cx="18" cy="29" r="1.5"/></svg>Free Wi-fi</div>
      <div class="tile"><svg viewBox="0 0 36 36"><path d="M11 5h14l-2 14a5 5 0 0 1-10 0zM18 24v7M12 31h12"/></svg>Minibar</div>
      <div class="tile"><svg viewBox="0 0 36 36"><path d="M4 24h28l-4 6H8zM10 24v-8h16v8M18 16V6l8 6"/></svg>Shuttle Boat<br>Service</div>
      <div class="tile"><svg viewBox="0 0 36 36"><rect x="4" y="18" width="28" height="12"/><circle cx="18" cy="9" r="4"/><path d="M12 18a6 6 0 0 1 12 0"/></svg>24-Hours Front<br>Desk</div>
      <div class="tile"><svg viewBox="0 0 36 36"><rect x="5" y="7" width="26" height="24" rx="2"/><path d="M5 14h26M11 4v6M25 4v6M11 20h4M21 20h4M11 26h4"/></svg>Check-In<br>11:00 am</div>
      <div class="tile"><svg viewBox="0 0 36 36"><circle cx="18" cy="18" r="13"/><path d="M18 10v8l5 4"/></svg>Check-Out<br>9:00 am</div>
      <div class="tile"><svg viewBox="0 0 36 36"><circle cx="18" cy="18" r="13"/><path d="M9 27L27 9M10 20h14v4H10z"/></svg>100% Smoke<br>Free</div>
    </div>
    <p class="call">Call Us ✆ (555) 013-4270</p>
    <span class="btn">Book Now!</span>
    <div class="partners">
      <span class="badge sq"></span>
      <span class="badge wide"></span>
      <span class="badge sq"></span>
      <span class="badge wide"></span>
      <span class="badge wide" style="width:90px;height:40px"></span>
      <span class="badge wide"></span>
    </div>
  </section>

  <div class="map" role="img" aria-label="Map of the coastline showing the resort location"></div>
  <div class="contact-band"></div>

  <section class="contact">
    <div class="contact-info">
      <h5>Contact Us</h5>
      <div class="row"><svg viewBox="0 0 24 24"><path d="M5 3h4l2 5-2.5 1.5a11 11 0 0 0 6 6L16 13l5 2v4a2 2 0 0 1-2 2A16 16 0 0 1 3 5a2 2 0 0 1 2-2z"/></svg><span>506-0100-2200<br>555-013-4270</span></div>
      <div class="row" style="margin-top:14px"><svg viewBox="0 0 24 24"><rect x="2" y="5" width="20" height="14"/><path d="M2 5l10 8 10-8"/></svg><span style="font-size:10px">info@ramasolvento.com</span></div>
      <div class="row" style="margin-top:14px"><svg viewBox="0 0 24 24"><path d="M12 22s7-7 7-12a7 7 0 0 0-14 0c0 5 7 12 7 12z"/><circle cx="12" cy="10" r="2.5"/></svg><span><small>Rama Sol Vento:<br>Bahía Serena, Península Norte, Costa Rica</small></span></div>
      <span class="btn-dir">Get Directions</span>
      <div class="socials"><span></span><span></span><span></span><span></span><span></span><span></span></div>
    </div>
    <div class="contact-form">
      <h5>Send Us a Message</h5>
      <div class="in">Your Name</div>
      <div class="in">Email</div>
      <div class="in">Phone</div>
      <div class="in">Subject</div>
      <div class="in msg">Message ...</div>
      <span class="btn">Submit</span>
    </div>
  </section>

  <footer class="footer">
    <div class="brand"><span class="brand-dot"></span><span class="brand-name">RAMA SOL VENTO</span></div>
    <p>© 2024 Rama Sol Vento. All Right Reserved</p>
  </footer>
  <svg class="to-top" viewBox="0 0 16 16"><path d="M3 14L8 2l5 12M5 10h6"/></svg>

</div>
</body>
</html>
```